I.T Managed services requires company brochure.

We are want a design to show our clients what we are all about.

Information about our company and our services can be found on our website, www.zorvane.com.au

We want a corporate design but yet still fun and attractive.

I have also uploaded my LOGO, please incorporate it into the design.
Updates

Hi All

I am not 100% happy with the designs provided.   Please visit our web page
www.zorvane.com.au
We need the following
• - 4 page brochure of a4
• - the first page to have our logo on it with details from our phone number, web site address and info email address, at the back of it to have our 4 core services which are managed Services, Backup Solutions, Disaster Recovery Solutions and Remote Access management similar to our web site
• - the second page to have about us
• - the third page to have our services we offer and information
• - the fourth page to why us tab
• We want the brochure to be in 4 pages, to be back to front, no cartoon characters and to look professional and modern - to be similar matched to our web site.
can you please email me on malcolm@zorvane.com.au

Target Market(s)

Small to medium sized companies (1-200 employees)

Industry/Entity Type

It Company

Requirements
Must have
• Must elaborate on the 4 core product of ZRVN, which are

- Managed I.T Services
- Backup Management
- Disaster Recovery
- Remote Access

Also would like it to be in an A3 size format that folds into A4 by the slides folding in on either side.

Use the PDF example I uploaded as a guide for the look of the brochure.
Nice to have
• I have upload a brochure I found about solar power, I like the look of the brochure and want my brochure to be similar.

```html
<!DOCTYPE html>
<html lang="en">
<head>
<meta charset="utf-8">
<title>Zorvane brochure cover spread</title>
<link rel="stylesheet" href="https://fonts.googleapis.com/css2?family=Mulish:wght@400;600&display=swap">
<style>
  :root {
    --page: #ffffff;
    --panel: #333333;
    --orange: #ee5127;
    --bar: #e9542a;
    --white: #ffffff;
    --muted: #d2d2d2;
    --url: #bdbdbd;
    --blue: #0ba7e1;
    --magenta: #c42a8c;
    --green: #6e8f3c;
    --amber: #f5a31a;
    --rust: #b2402c;
    --brown: #a97a30;
    --ring: #8a8a8a;
    --icon-grey: #bbbbbb;
    --logo-red: #d32630;
  }
  * { margin: 0; padding: 0; box-sizing: border-box; }
  html, body {
    width: 1200px; height: 885px; overflow: hidden;
    background: var(--page);
    font-family: "Mulish", sans-serif;
  }
  .spread {
    position: absolute; left: 45px; top: 48px;
    width: 1112px; height: 786px;
    background: var(--panel);
    overflow: hidden;
    box-shadow: 2px 3px 6px rgba(0,0,0,.35);
  }
  .abs { position: absolute; }
  .site-url { left: 985px; top: 39px; font-size: 11px; color: var(--url); }

  .brand { color: var(--white); font-weight: 600; letter-spacing: 3px; text-transform: uppercase; white-space: nowrap; display: flex; align-items: center; }
  .brand .dot { border-radius: 50%; background: var(--logo-red); display: inline-block; }
  .brand-small { left: 200px; top: 135px; font-size: 24px; gap: 10px; }
  .brand-small .dot { width: 14px; height: 14px; }
  .brand-large { left: 700px; top: 270px; font-size: 52px; gap: 18px; }
  .brand-large .dot { width: 28px; height: 28px; }

  .service-icon { width: 58px; height: 58px; }
  .service-title { font-size: 13px; color: var(--orange); font-weight: 600; white-space: nowrap; }
  .service-intro { font-size: 9.5px; color: var(--muted); line-height: 11px; width: 160px; }
  .service-list { list-style: none; font-size: 11px; color: var(--muted); line-height: 13.5px; }
  .service-list li::before { content: "• "; }

  .contacts-title { left: 52px; top: 606px; font-size: 34px; font-weight: 400; color: var(--white); }
  .contact-bar {
    left: 0; top: 656px; width: 410px; height: 41px;
    background: var(--bar); border-radius: 0 8px 8px 0;
    color: var(--white); font-size: 11px; padding: 5px 0 0 50px; line-height: 17px;
  }
  .contact-line { display: flex; align-items: center; gap: 15px; }
  .contact-line svg { margin-right: -11px; }

  .tagline-bar {
    left: 702px; top: 657px; width: 410px; height: 41px;
    background: var(--bar); border-radius: 8px 0 0 8px;
    color: var(--white); font-size: 27px; line-height: 41px; padding-left: 22px;
  }
</style>
</head>
<body>
<main class="spread">
  <div class="abs site-url">www.zorvane.com.au</div>

  <!-- Left panel -->
  <div class="abs brand brand-small"><span class="dot"></span>Zorvane</div>

  <svg class="abs service-icon" style="left:52px;top:221px" viewBox="0 0 58 58">
    <circle cx="29" cy="29" r="28" fill="#fff"/><circle cx="29" cy="29" r="23" fill="var(--blue)"/>
    <rect x="17" y="18" width="24" height="17" rx="2" fill="none" stroke="#fff" stroke-width="2"/>
    <path d="M25 39h8M29 35v4" stroke="#fff" stroke-width="2"/>
  </svg>
  <div class="abs service-title" style="left:116px;top:242px">Home Computer Services</div>
  <div class="abs service-intro" style="left:116px;top:262px;width:200px">We cater for all your IT needs everyday.</div>
  <ul class="abs service-list" style="left:117px;top:284px">
    <li>Advise</li><li>Phone Support</li><li>Remote Support</li><li>Software Sales</li><li>Hardware Sales</li>
  </ul>

  <svg class="abs service-icon" style="left:295px;top:221px" viewBox="0 0 58 58" role="img" aria-label="Icon of two support staff">
    <circle cx="29" cy="29" r="28" fill="#fff"/><circle cx="29" cy="29" r="23" fill="var(--magenta)"/>
  </svg>
  <div class="abs service-title" style="left:362px;top:244px">Business Computer Services</div>
  <div class="abs service-intro" style="left:362px;top:262px;width:200px">ZRVN Specialises in SME market</div>
  <ul class="abs service-list" style="left:362px;top:282px">
    <li>End to end IT support</li><li>24/7 Support hotline</li><li>24/7 System monitoring</li><li>Backups</li><li>Disaster Recovery</li>
  </ul>

  <svg class="abs service-icon" style="left:52px;top:401px" viewBox="0 0 58 58">
    <circle cx="29" cy="29" r="28" fill="#fff"/><circle cx="29" cy="29" r="23" fill="var(--green)"/>
    <g fill="none" stroke="#fff" stroke-width="1.8">
      <circle cx="29" cy="29" r="13"/><ellipse cx="29" cy="29" rx="6" ry="13"/><path d="M16 29h26M18 22h22M18 36h22"/>
    </g>
  </svg>
  <div class="abs service-title" style="left:115px;top:423px">Nationwide IT Services</div>
  <div class="abs service-intro" style="left:115px;top:441px">We have offices and representatives nationwide</div>
  <ul class="abs service-list" style="left:113px;top:474px">
    <li>Victoria HQ</li><li>New South Wales</li><li>Tasmania</li><li>South Australia</li><li>Queensland</li>
  </ul>

  <svg class="abs service-icon" style="left:295px;top:401px" viewBox="0 0 58 58">
    <circle cx="29" cy="29" r="28" fill="#fff"/><circle cx="29" cy="29" r="23" fill="var(--amber)"/>
  </svg>
  <div class="abs service-title" style="left:362px;top:423px">Internet Services</div>
  <div class="abs service-intro" style="left:362px;top:441px">Wide range of Internet Services to our clients</div>
  <ul class="abs service-list" style="left:362px;top:473px">
    <li>Cloud</li><li>Website Design</li><li>Website Hosting</li><li>VPN connectivity</li><li>Social Media Promotions</li>
  </ul>

  <h2 class="abs contacts-title">Our Contacts</h2>
  <div class="abs contact-bar">
    <div>48 Harlow Lane North Ferndale, Victoria 3099</div>
    <div class="contact-line">
      <svg width="13" height="13" viewBox="0 0 13 13"><circle cx="6.5" cy="6.5" r="5.7" fill="none" stroke="#fff" stroke-width="1.2"/><path d="M4.5 3.5c0 3 2 5.5 4.5 5.8" fill="none" stroke="#fff" stroke-width="1.6"/></svg>
      <span>+61 9555 0142</span><span>www.zorvane.com.au</span><span>info@zorvane.com.au</span>
    </div>
  </div>

  <!-- Right panel -->
  <div class="abs brand brand-large"><span class="dot"></span>Zorvane</div>

  <svg class="abs" style="left:620px;top:340px" width="492" height="310" viewBox="620 340 492 310">
    <circle cx="682" cy="473" r="50" fill="var(--ring)"/><circle cx="682" cy="473" r="42" fill="var(--rust)"/>
    <path d="M682 450v26" stroke="#fff" stroke-width="8" stroke-linecap="round"/><circle cx="682" cy="490" r="5" fill="#fff"/>

    <circle cx="876" cy="561" r="77" fill="var(--ring)"/><circle cx="876" cy="561" r="66" fill="var(--brown)"/>
    <path d="M846 535h60a10 10 0 0 1 10 10v26a10 10 0 0 1-10 10h-34l-16 14v-14h-10a10 10 0 0 1-10-10v-26a10 10 0 0 1 10-10z" fill="none" stroke="#9a9a9a" stroke-width="6"/>

    <circle cx="746" cy="536" r="63" fill="#fff"/><circle cx="746" cy="536" r="55" fill="var(--magenta)" role="img" aria-label="Icon of two support staff"/>

    <circle cx="1075" cy="407" r="48" fill="var(--ring)"/><circle cx="1075" cy="407" r="40" fill="var(--green)"/>
    <g fill="var(--icon-grey)">
      <rect x="1069" y="383" width="12" height="48" rx="2"/>
      <rect x="1069" y="383" width="12" height="48" rx="2" transform="rotate(45 1075 407)"/>
      <rect x="1069" y="383" width="12" height="48" rx="2" transform="rotate(90 1075 407)"/>
      <rect x="1069" y="383" width="12" height="48" rx="2" transform="rotate(135 1075 407)"/>
      <circle cx="1075" cy="407" r="17"/>
    </g>
    <circle cx="1075" cy="407" r="7" fill="var(--green)"/>

    <circle cx="992" cy="493" r="80" fill="#fff"/><circle cx="992" cy="493" r="72" fill="var(--blue)"/>
    <rect x="950" y="458" width="84" height="58" rx="6" fill="none" stroke="#fff" stroke-width="5"/>
    <path d="M978 534h28M992 516v18" stroke="#fff" stroke-width="5"/>
  </svg>

  <div class="abs tagline-bar">support anytime, anywhere!</div>
</main>
</body>
</html>
```